Book cover for "Steady Harbor" focused on scaling up an Insurance Agency

Front Cover:
We need book cover for our upcoming book with title "Steady Harbor" . Subtitle of book is "The secrets behind building a multi-million dollar Insurance agency:Interviews, success stories and framework for success".
On top line it should say " Foreword by Mark Vellison".
Author name : "Rajendra Kulkat"
This book will help insurance agents in scaling up their agency. It will also help someone looking to start a business or side hustle.

Back Cover:
It should contain content provided below and image of author attached.
"
Who should read this book?

Do you know that starting an Insurance Agency is probably one of the best business ideas?
Do you want to know how some startups created billion dollar plus insurance based companies in the last 5-10 years?
Do you want to know the secrets behind building a multi-million dollar Insurance agency?
Do you want to know how to scale up an Insurance Agency profitably?
Do you want to know how to cut through the noise in the market and differentiate your business?
How to leverage technology to rise above (be seen and heard) the myriad of agencies around you and compete with both local and online agencies?
How to build a team which carries your mindset to take care of clients and grow your business?
(above list should be bulleted)
If you are interested in learning about these topics then you are at the right place.

You can either spend years figuring out things yourself or read this book and get wisdom from successful agents and thought leaders at top insurance agencies."

Spine:
" Steady Harbor by Rajendra Kulkat"

Requirements:
One file should be only book cover.
Other file should contain :front cover, back cover and spine as one file.
It should follow standard for Brimlow Press, link provided below.
https://print.brimlowpress.example/en_US/help/topic/Q738210465

Target Market(s)

Insurance Agents
People looking to start a new business
Side Hustlers

Industry/Entity Type

Insurance Agency

Font styles to use
Serif

```html
<!DOCTYPE html>
<html lang="en">
<head>
<meta charset="utf-8">
<title>Steady Harbor – Full Cover</title>
<link rel="stylesheet" href="https://fonts.googleapis.com/css2?family=PT+Serif:wght@400;700&family=Archivo+Narrow:wght@400;600&display=swap">
<style>
  :root{
    --sage:#617c5f;
    --tan:#dcc1a9;
    --ink:#3a3a3a;
    --deep-green:#1f5a2b;
    --white:#ffffff;
    --code-box:#edf0d2;
  }
  *{margin:0;padding:0;box-sizing:border-box}
  html,body{width:1200px;height:800px;overflow:hidden;background:var(--sage)}
  .cover{position:relative;width:1200px;height:800px;background:var(--sage);font-family:"PT Serif",serif;color:var(--white)}

  /* Back cover */
  .back-heading{position:absolute;left:106px;top:136px;font-size:18.5px;font-weight:700;white-space:nowrap}
  .back-panel{position:absolute;left:96px;top:176px;width:441px;height:528px;background:var(--tan);border-bottom-left-radius:38px}
  .author-photo{position:absolute;left:376px;top:128px;width:152px;height:166px;border:4px solid var(--tan);z-index:2;
    background:linear-gradient(180deg,#eceef0 0%,#d9dde2 45%,#8e9cb2 70%,#5b6b86 100%)}
  .questions{position:absolute;left:118px;top:190px;width:402px;font-family:"Archivo Narrow",sans-serif;font-size:11.6px;line-height:14px;color:var(--ink);list-style:none}
  .photo-clearance{float:right;width:150px;height:110px}
  .questions li{margin-bottom:2px}
  .questions li::before{content:"•"}
  .invitation{position:absolute;left:118px;top:476px;width:320px;font-family:"Archivo Narrow",sans-serif;font-size:11.6px;line-height:16px;color:var(--ink)}
  .promise{position:absolute;left:118px;top:522px;width:418px;font-family:"Archivo Narrow",sans-serif;font-weight:600;font-size:11.6px;line-height:16px;color:var(--deep-green)}
  .code-area{position:absolute;left:318px;top:590px;width:196px;height:104px;background:var(--code-box)}

  /* Spine */
  .spine{position:absolute;left:572px;top:236px;writing-mode:vertical-rl;white-space:nowrap}
  .spine-title{font-size:27px;font-weight:700}
  .spine-author{font-size:12px;font-weight:700;margin-top:6px}

  /* Front cover */
  .front-title{position:absolute;left:670px;width:490px;top:70px;text-align:center;font-size:40px;font-weight:700}
  .front-author{position:absolute;left:758px;top:132px;font-size:15px;font-weight:700}
  .front-photo{position:absolute;left:670px;top:176px;width:490px;height:454px;border-top-right-radius:10px;
    background:linear-gradient(160deg,#d6d4cf 0%,#f1f1ee 35%,#c9c3ba 60%,#8f857a 85%,#6d655d 100%)}
  .foreword{position:absolute;left:670px;width:490px;top:634px;text-align:center;font-size:11px;font-weight:700}
  .subtitle{position:absolute;left:650px;width:530px;top:652px;text-align:center;font-size:12px;line-height:15px;font-weight:700}
</style>
</head>
<body>
<main class="cover">
  <section class="back-cover">
    <h2 class="back-heading">Who should read this book?</h2>
    <div class="back-panel"></div>
    <div class="author-photo" role="img" aria-label="Portrait of the author in a light blue blazer"></div>
    <ul class="questions">
      <div class="photo-clearance"></div>
      <li>Do you know that starting an Insurance Agency is probably one of the best business ideas?</li>
      <li>Do you want to know how some startups created billion dollar plus insurance based companies in the last 5-10 years?</li>
      <li>Do you want to know the secrets behind building a multi-million dollar Insurance agency?</li>
      <li>Do you want to know how to scale up an Insurance Agency profitably?</li>
      <li>Do you want to know how to cut through the noise in the market and differentiate your business?</li>
      <li>How to leverage technology to rise above (be seen and heard) the myriad of agencies around you and compete with both local and online agencies?</li>
      <li>How to build a team which carries your mindset to take care of clients and grow your business?</li>
    </ul>
    <p class="invitation">If you are interested in learning about these topics<br>then you are at the right place.</p>
    <p class="promise">You can either spend years figuring out things yourself or read this book and get wisdom from successful agents and thought leaders at top insurance agencies.</p>
    <div class="code-area"></div>
  </section>

  <section class="spine">
    <span class="spine-title">Steady Harbor</span>
    <span class="spine-author">by Rajendra Kulkat</span>
  </section>

  <section class="front-cover">
    <h1 class="front-title">Steady Harbor</h1>
    <p class="front-author">by Rajendra Kulkat</p>
    <div class="front-photo" role="img" aria-label="Business presenter speaking to colleagues seated at a meeting table with laptops in a bright office"></div>
    <p class="foreword">Foreword by Mark Vellison</p>
    <p class="subtitle">"The secrets behind building a multi-million dollar Insurance agency:<br>Interviews, success stories and framework for success".</p>
  </section>
</main>
</body>
</html>
```